Talbrin Business Cards

Front and back. Simon Kavelle MBA is the CEO of Talbrin Homes. Black white and grays. Logo and cool design.

Target Market(s)

Professional lenders and investors

Industry/Entity Type

Real estate developer. NO HOUSES OR ROOFS

Contact Information for Business Card

Logo, name and unique design. Front and back. Simon Kavelle MBA is the CEO of Talbrin Homes. Black white and grays. Logo and cool design.

Font styles to use
Sans Serif

Colors

Designer to choose only greyscale colors for use in the design.

Requirements
Must have
• Cool look. Not the same card I could design.
Nice to have
• Something memorable
Should not have
• Basic

```html
<!DOCTYPE html>
<html lang="en">
<head>
<meta charset="utf-8">
<title>Talbrin Homes – Business Cards</title>
<link href="https://fonts.googleapis.com/css2?family=Montserrat:wght@400;600;800&display=swap" rel="stylesheet">
<style>
  :root {
    --page: #d9d9d9;
    --card-white: #ffffff;
    --card-black: #0a0a0a;
    --ink: #0b0b0b;
    --ink-soft: #222222;
    --watermark: #2b2b2b;
    --rule: #8a8a8a;
    --silver-light: #f2f2f2;
    --silver-dark: #8c8c8c;
  }
  html, body {
    margin: 0;
    padding: 0;
    width: 1200px;
    height: 900px;
    overflow: hidden;
    background: var(--page);
  }
  .canvas {
    position: relative;
    width: 1200px;
    height: 900px;
  }
  .card {
    position: absolute;
    width: 560px;
    height: 320px;
    box-shadow: 0 10px 28px rgba(0,0,0,0.22);
    background: var(--card-white);
  }
  .card svg { display: block; }
  .card--front { left: 120px; top: 100px; }
  .card--back  { left: 520px; top: 480px; }
  .wordmark {
    font-family: "Montserrat", sans-serif;
    font-weight: 800;
    fill: var(--ink);
    letter-spacing: -1px;
  }
  .watermark {
    font-family: "Montserrat", sans-serif;
    font-weight: 800;
    fill: var(--watermark);
    letter-spacing: -1px;
  }
  .holder-name {
    font-family: "Montserrat", sans-serif;
    font-weight: 800;
    fill: var(--ink);
    font-size: 22px;
  }
  .holder-title {
    font-family: "Montserrat", sans-serif;
    font-weight: 400;
    fill: var(--ink-soft);
    font-size: 20px;
  }
</style>
</head>
<body>
<main class="canvas">

  <section class="card card--front" aria-label="Business card front">
    <svg width="560" height="320" viewBox="0 0 560 320">
      <defs>
        <linearGradient id="silver-front" x1="0" y1="0" x2="1" y2="1">
          <stop offset="0" stop-color="var(--silver-dark)"/>
          <stop offset="0.5" stop-color="var(--silver-light)"/>
          <stop offset="1" stop-color="var(--silver-dark)"/>
        </linearGradient>
        <linearGradient id="paper-front" x1="0" y1="0" x2="1" y2="1">
          <stop offset="0" stop-color="#f4f4f4"/>
          <stop offset="1" stop-color="#ffffff"/>
        </linearGradient>
        <clipPath id="band-front">
          <polygon points="222,0 560,0 560,278"/>
        </clipPath>
      </defs>
      <rect class="paper" width="560" height="320" fill="url(#paper-front)"/>
      <polygon class="silver-stripe" points="200,0 222,0 560,278 560,300" fill="url(#silver-front)"/>
      <polygon class="black-band" points="222,0 560,0 560,278" fill="var(--card-black)"/>
      <g clip-path="url(#band-front)">
        <text class="watermark" font-size="52" transform="translate(300,40) rotate(39.5)">Talbrin Homes</text>
      </g>
      <text class="wordmark" x="30" y="212" font-size="46">Talbrin Homes</text>
    </svg>
  </section>

  <section class="card card--back" aria-label="Business card back">
    <svg width="560" height="320" viewBox="0 0 560 320">
      <defs>
        <linearGradient id="silver-back" x1="0" y1="0" x2="1" y2="1">
          <stop offset="0" stop-color="var(--silver-dark)"/>
          <stop offset="0.5" stop-color="var(--silver-light)"/>
          <stop offset="1" stop-color="var(--silver-dark)"/>
        </linearGradient>
        <linearGradient id="paper-back" x1="0" y1="0" x2="1" y2="1">
          <stop offset="0" stop-color="#f4f4f4"/>
          <stop offset="1" stop-color="#ffffff"/>
        </linearGradient>
        <clipPath id="band-back">
          <polygon points="0,112 0,320 328,320"/>
        </clipPath>
      </defs>
      <rect class="paper" width="560" height="320" fill="url(#paper-back)"/>
      <polygon class="silver-stripe" points="0,94 0,112 328,320 352,320" fill="url(#silver-back)"/>
      <polygon class="black-band" points="0,112 0,320 328,320" fill="var(--card-black)"/>
      <g clip-path="url(#band-back)">
        <text class="watermark" font-size="50" transform="translate(250,300) rotate(212.5)">Talbrin Homes</text>
      </g>
      <text class="wordmark" x="528" y="126" font-size="44" text-anchor="end">Talbrin Homes</text>
      <line class="divider" x1="250" y1="150" x2="560" y2="150" stroke="var(--rule)" stroke-width="1"/>
      <text class="holder-name" x="528" y="186" text-anchor="end">SIMON KAVELLE</text>
      <text class="holder-title" x="528" y="214" text-anchor="end">MBA | CEO</text>
    </svg>
  </section>

</main>
</body>
</html>
```